Tradelo Size Charts - 6 Products

Hi Koby,

I had you in mind for this, but we have a new e-commerce store that requires the attached 6 size charts re-designed. They are terrible charts from drop shippers and we need them re-designed to match the Talvoro brand logo to designed.

Chart needs to be white background and black letter's. You can add some smart gradients or design to it if you want to make it look elegant and confident.

Can you design 1 chart and we can amend it to perfection with feedback?
Once we agree on the style - you can then do the same style and design for the remaining charts.

Let me know if this is ok?

```html
<!DOCTYPE html>
<html lang="en">
<head>
<meta charset="utf-8">
<title>Size Chart</title>
<link rel="stylesheet" href="https://fonts.googleapis.com/css2?family=Montserrat:wght@500;600;700&display=swap">
<style>
  :root {
    --ink: #111111;
    --ink-soft: #2b2b2b;
    --label-bg: #232324;
    --label-text: #ffffff;
    --rule: #1a1a1a;
    --grid-line: #9e9e9e;
    --row-1: #d9d9d7;
    --row-2: #e0e0e0;
    --row-3: #e6e6e6;
    --row-4: #eeeeee;
    --row-5: #fbfbfb;
    --page: #ffffff;
  }
  * { box-sizing: border-box; margin: 0; padding: 0; }
  html, body {
    width: 1200px;
    height: 938px;
    overflow: hidden;
    background: var(--page);
  }
  body {
    position: relative;
    font-family: "Montserrat", Arial, sans-serif;
    color: var(--ink);
  }
  .chart-heading {
    position: absolute;
    top: 138px;
    left: 69px;
    width: 1080px;
    display: flex;
    align-items: center;
    gap: 22px;
  }
  .chart-heading__rule {
    flex: 1;
    height: 1px;
    background: var(--rule);
  }
  .chart-heading__title {
    font-size: 32px;
    font-weight: 700;
    letter-spacing: 5px;
    color: var(--ink-soft);
    line-height: 42px;
  }
  .chart-subtitle {
    position: absolute;
    top: 186px;
    left: 0;
    width: 1228px;
    text-align: center;
    font-size: 15px;
    font-weight: 500;
    color: var(--ink-soft);
    letter-spacing: 0.3px;
  }
  .size-table {
    position: absolute;
    top: 232px;
    left: 57px;
    width: 1092px;
    display: grid;
    grid-template-columns: 271px 273px 266px 282px;
    grid-template-rows: 88px 90px 90px 90px 87px;
    border: 1px solid var(--grid-line);
  }
  .size-row { display: contents; }
  .size-label {
    background: var(--label-bg);
    color: var(--label-text);
    font-size: 22px;
    font-weight: 700;
    display: flex;
    align-items: center;
    padding-left: 68px;
    border-bottom: 1px solid #3a3a3a;
  }
  .size-cell {
    display: flex;
    align-items: center;
    justify-content: center;
    font-size: 17px;
    font-weight: 500;
    color: var(--ink);
    border-left: 1px solid var(--grid-line);
    border-bottom: 1px solid var(--grid-line);
  }
  .size-row:last-child .size-cell,
  .size-row:last-child .size-label { border-bottom: none; }
  .size-row--s .size-cell { background: var(--row-1); }
  .size-row--m .size-cell { background: var(--row-2); }
  .size-row--l .size-cell { background: var(--row-3); }
  .size-row--xl .size-cell { background: var(--row-4); }
  .size-row--2xl .size-cell { background: var(--row-5); }

  .notes {
    position: absolute;
    top: 712px;
    left: 57px;
  }
  .notes__title {
    font-size: 22px;
    font-weight: 700;
    color: var(--ink-soft);
    margin-bottom: 16px;
  }
  .notes__list { list-style: none; }
  .notes__item {
    position: relative;
    padding-left: 30px;
    font-size: 14px;
    font-weight: 500;
    color: var(--ink-soft);
    line-height: 29px;
  }
  .notes__item::before {
    content: "";
    position: absolute;
    left: 9px;
    top: 12px;
    width: 6px;
    height: 6px;
    border-radius: 50%;
    background: var(--ink);
  }
</style>
</head>
<body>
  <header class="chart-heading">
    <span class="chart-heading__rule"></span>
    <h1 class="chart-heading__title">SIZE CHART</h1>
    <span class="chart-heading__rule"></span>
  </header>
  <p class="chart-subtitle">SIZE CHART (UNIT:- CM/INCH)</p>

  <section class="size-table" aria-label="Size measurements">
    <div class="size-row size-row--s">
      <div class="size-label">SIZE : S</div>
      <div class="size-cell">BUST: 90CM/35.4”</div>
      <div class="size-cell">WAIST: 98CM/38.6”</div>
      <div class="size-cell">LENGTH: 81CM/31.5”</div>
    </div>
    <div class="size-row size-row--m">
      <div class="size-label">SIZE : M</div>
      <div class="size-cell">BUST: 94CM/37”</div>
      <div class="size-cell">WAIST: 102CM/40.2”</div>
      <div class="size-cell">LENGTH: 81CM/31.9”</div>
    </div>
    <div class="size-row size-row--l">
      <div class="size-label">SIZE : L</div>
      <div class="size-cell">BUST: 98CM/38.6”</div>
      <div class="size-cell">WAIST: 106CM/41.7”</div>
      <div class="size-cell">LENGTH: 82CM/32.3”</div>
    </div>
    <div class="size-row size-row--xl">
      <div class="size-label">SIZE : XL</div>
      <div class="size-cell">BUST: 102CM/40.2”</div>
      <div class="size-cell">WAIST: 110CM/43.3”</div>
      <div class="size-cell">LENGTH: 83CM/33.7”</div>
    </div>
    <div class="size-row size-row--2xl">
      <div class="size-label">SIZE : 2XL</div>
      <div class="size-cell">BUST: 106CM/41.7”</div>
      <div class="size-cell">WAIST: 114CM/44.9”</div>
      <div class="size-cell">LENGTH: 84CM/33.1”</div>
    </div>
  </section>

  <section class="notes">
    <h2 class="notes__title">NOTES :-</h2>
    <ul class="notes__list">
      <li class="notes__item">PLEASE ALLOW 1-2 CM MEASURING DEVIATION DUE TO MANUAL MEASUREMENT.</li>
      <li class="notes__item">PLEASE CHECK THE SIZE CHART BEFORE ORDER.</li>
      <li class="notes__item">IF YOU ARE NOT SURE THE SIZE, PLEASE SEND MESSAGE TO US.</li>
    </ul>
  </section>
</body>
</html>
```